Home page for local retail aggregator

About us: We are a new company that showcases beautiful products available at nearby retail stores. This homepage is meant to display the latest products featured on our site and also allow the user to search, browse with filters, and access their account details.

Currently, our home page looks a little bland. We want the focus of the site to remain on the featured photos and products but the design should be more cohesive. The most successful designs will make more subtle use of our colors, provide intuitive menu controls, and look visually stunning.

This homepage has a few sections:

Header:
-Top Section: will always remain at the top of the page. There should be space for our company name ”zAntelope”, a tagline, and a place for the menus.
-Menus: user must be able to find links for: “My profile” “My Products” “Add Product” “Preview store”
-Bottom section: this will scroll with the user and always remain at the top of the screen providing access to a search box, and filters for “location” “price” and retail categories.

Main Page:
-Each product featured is shown on a tile that includes a photo, title, price, name of store, has space to leave a comment, and include counters for "likes," comments, and "Pods"). “Pods” are bookmark folders. The user’s profile pic is also shown in miniature if they leave a comment.

The final version of the site must be delivered in a fully layered photoshop file and have versions demonstrating what the page will look like both when a user is logged-in and when logged-out.

Target Market(s)

Most of our users are female 18-45. Our customers are retail store owners who want their products to look attractive and professional.

Industry/Entity Type

Retail

Requirements
Must have
• Our logo must be present on the site (attached to project). You're welcome to change the colors in the header but it should look good with our logo.

For reference here are colors we're currently using:
Site text is in Dark Blue: RGB(10/23/47)
Logo color on business cards is light blue: (51/153/204)
Nice to have
• Would love to see new versions of the menus that are more modern and intuitive. Currently we just have links to each individual control. Putting these in a drop-down or re-arranging them would be nice.

```html
<!DOCTYPE html>
<html lang="en">
<head>
<meta charset="utf-8">
<title>zAntelope – Local product search and discovery</title>
<link rel="stylesheet" href="https://fonts.googleapis.com/css2?family=Ubuntu:wght@400;500;700&family=Tinos&display=swap">
<style>
:root{
  --teal:#1aa6c6;
  --teal-light:#4fc3dc;
  --navy:#0a172f;
  --panel:#03252a;
  --tile:#efefef;
  --tile-edge:#d2d2d2;
  --bar:#3f8fd2;
  --grey:#7a7a7a;
  --link:#2e7fd0;
  --like:#8b3fb3;
  --foot-light:#57bfd6;
  --foot-dark:#3c8ed3;
  --white:#fff;
}
*{box-sizing:border-box;margin:0;padding:0}
html,body{width:1200px;height:1002px;overflow:hidden;background:var(--white);font-family:"Ubuntu",sans-serif}
.page{position:relative;width:1200px;height:1002px}
.header{position:absolute;left:40px;top:0;width:1120px;height:205px}
.header-band{position:absolute;left:0;top:0}
.brand{position:absolute;left:72px;top:38px;color:var(--navy)}
.brand-name{font-size:29px;font-weight:500;letter-spacing:.5px;line-height:1}
.brand-tagline{font-size:16px;margin-top:8px}
.mascot{position:absolute;left:440px;top:6px;width:230px;height:190px;border-radius:50% 50% 40% 40%;background:radial-gradient(circle at 50% 35%,#6fc4ee 0,#2f86cf 55%,rgba(47,134,207,0) 72%)}
.account-nav{position:absolute;left:859px;top:36px;display:flex;gap:22px;color:var(--white);font-size:15px}
.follow{position:absolute;left:1059px;top:12px;color:var(--white);font-size:9px}
.social{position:absolute;left:1016px;top:30px;display:flex;gap:6px}
.social span{color:var(--white);font-size:9px;font-weight:500}
.bag{position:absolute;right:20px;top:69px;text-align:right;color:var(--white)}
.bag-title{font-size:15px}
.bag-count{font-family:"Tinos",serif;font-size:14px;margin-top:6px;word-spacing:2px}
.sub-nav{position:absolute;left:44px;top:166px;display:flex;gap:9px;color:var(--grey);font-size:15px}
.search-label{position:absolute;left:846px;top:166px;color:var(--grey);font-size:15px}
.search-box{position:absolute;left:900px;top:162px;width:200px;height:28px;border-radius:4px;background:#f6f6f6;border:1px solid #ccc;box-shadow:0 1px 3px rgba(0,0,0,.25) inset}
.search-clear{position:absolute;right:8px;top:6px}
.catalog{position:absolute;left:40px;top:205px;width:1120px;height:640px;background:var(--panel)}
.row-rule{position:absolute;left:18px;top:320px;width:1083px;height:1px;background:#3c5c60}
.tile{position:absolute;width:202px;height:244px;background:var(--tile);border-radius:3px;box-shadow:0 0 0 1px var(--tile-edge) inset}
.tile-photo{position:absolute;left:7px;top:7px;width:188px;height:146px}
.tile-zoom{position:absolute;right:8px;top:16px}
.tile-title{position:absolute;left:5px;top:163px;width:192px;height:29px;border-radius:4px;background:var(--bar);color:var(--white);font-size:15px;line-height:30px;padding-left:7px}
.tile-label{position:absolute;left:9px;top:198px;color:var(--grey);font-size:12.5px}
.tile-stats{position:absolute;left:9px;top:217px;font-family:"Tinos",serif;font-size:9.5px;color:var(--link);white-space:nowrap}
.tile-stats .likes{color:var(--like)}
.tile-stats .pods{color:var(--navy)}
.tile-price{position:absolute;right:10px;top:200px;font-family:"Tinos",serif;font-size:29px;color:var(--navy);word-spacing:3px}
.tile-rule{position:absolute;left:7px;right:7px;top:232px;height:1px;background:#c4c4c4}
.pager{position:absolute;left:24px;top:609px;display:flex;align-items:center;color:var(--white);font-size:15px}
.pager .count{font-weight:700;margin-right:14px}
.pager .pages{margin-left:8px;display:flex;gap:8px}
.pager .current{background:#5b6d6f;padding:0 4px}
.next{position:absolute;left:541px;top:605px;color:var(--white);font-size:19px;font-weight:700;display:flex;align-items:center;gap:10px}
.payments{position:absolute;left:760px;top:860px;display:flex;gap:8px;color:var(--navy);font-size:10px;font-weight:500}
.footer-links{position:absolute;left:40px;top:890px;width:1120px;height:36px;background:var(--foot-light);display:flex;justify-content:center;gap:20px;color:var(--navy);font-size:15px;line-height:38px}
.footer-legal{position:absolute;left:40px;top:926px;width:1120px;height:26px;background:var(--foot-dark);color:var(--white);font-size:11.5px;text-align:center;line-height:26px}
</style>
</head>
<body>
<div class="page">
  <header class="header">
    <svg class="header-band" width="1120" height="205" viewBox="0 0 1120 205">
      <defs>
        <linearGradient id="band" x1="0" y1="0" x2="0" y2="1">
          <stop offset="0" stop-color="#169fc0"/>
          <stop offset="1" stop-color="#4ec4dc"/>
        </linearGradient>
      </defs>
      <path d="M0 0H1120V150C900 120 700 118 560 124C360 128 150 135 0 150Z" fill="url(#band)"/>
      <path d="M40 140C250 122 420 120 540 122" stroke="#ffffff" stroke-opacity=".6" stroke-width="2" fill="none"/>
      <path d="M620 120C800 118 980 122 1110 136" stroke="#ffffff" stroke-opacity=".6" stroke-width="2" fill="none"/>
    </svg>
    <div class="brand">
      <div class="brand-name">zAntelope</div>
      <div class="brand-tagline">Local product search and discovery</div>
    </div>
    <div class="mascot" role="img" aria-label="Blue mascot character surrounded by floating product icons"></div>
    <div class="follow">Follow us</div>
    <nav class="account-nav"><a>My Profile</a><a>Logout</a></nav>
    <div class="social"><span>Friendly</span><span>Chirp</span><span>Linkup</span></div>
    <div class="bag">
      <div class="bag-title">My bag</div>
      <div class="bag-count">iteams:&nbsp; 0 &nbsp;&nbsp; total:&nbsp; $ 0.00</div>
    </div>
    <nav class="sub-nav"><a>My Products</a><span>·</span><a>Add Product</a><span>·</span><a>Preview stor</a></nav>
    <div class="search-label">Search</div>
    <div class="search-box">
      <svg class="search-clear" width="14" height="14" viewBox="0 0 14 14"><circle cx="7" cy="7" r="6" fill="#9a9a9a"/><path d="M4.5 4.5L9.5 9.5M9.5 4.5L4.5 9.5" stroke="#fff" stroke-width="1.5"/></svg>
    </div>
  </header>

  <main class="catalog">
    <article class="tile" style="left:18px;top:55px">
      <div class="tile-photo" role="img" aria-label="Dark tablet case packaging boxes" style="background:linear-gradient(#f4f4f4,#4a4a4a 60%,#eaeaea)"></div>
      <svg class="tile-zoom" width="22" height="22" viewBox="0 0 22 22"><circle cx="9" cy="9" r="8" fill="none" stroke="#999"/><path d="M9 5V13M5 9H13M15 15L21 21" stroke="#999"/></svg>
      <div class="tile-title">Products</div><div class="tile-label">Minimal price</div>
      <div class="tile-stats"><span class="likes">5 likes</span>&nbsp; 0 comments <span>0 pods</span></div>
      <div class="tile-price">$ 60</div><div class="tile-rule"></div>
    </article>
    <article class="tile" style="left:238px;top:55px">
      <div class="tile-photo" role="img" aria-label="Earphones with geometric patterned box" style="background:linear-gradient(135deg,#f7f7f7,#4d8d94 55%,#f2f2f2)"></div>
      <svg class="tile-zoom" width="22" height="22" viewBox="0 0 22 22"><circle cx="9" cy="9" r="8" fill="none" stroke="#999"/><path d="M9 5V13M5 9H13M15 15L21 21" stroke="#999"/></svg>
      <div class="tile-title">Products</div><div class="tile-label">Minimal price</div>
      <div class="tile-stats"><span class="likes">2 likes</span>&nbsp; 0 comments 0 pods</div>
      <div class="tile-price">$ 75</div><div class="tile-rule"></div>
    </article>
    <article class="tile" style="left:459px;top:55px">
      <div class="tile-photo" role="img" aria-label="Shampoo and lotion bottles" style="background:linear-gradient(#fafafa,#d8d8d8 50%,#3a3a33)"></div>
      <svg class="tile-zoom" width="22" height="22" viewBox="0 0 22 22"><circle cx="9" cy="9" r="8" fill="none" stroke="#999"/><path d="M9 5V13M5 9H13M15 15L21 21" stroke="#999"/></svg>
      <div class="tile-title">Products</div><div class="tile-label">Minimal price</div>
      <div class="tile-stats"><span class="likes">5 likes</span>&nbsp; 0 comments <span class="pods">1 pods</span></div>
      <div class="tile-price">$ 30</div><div class="tile-rule"></div>
    </article>
    <article class="tile" style="left:678px;top:55px">
      <div class="tile-photo" role="img" aria-label="Kitchen gadget in a white box" style="background:linear-gradient(135deg,#cfcfcf,#f5f5f5 55%,#bdbdbd)"></div>
      <svg class="tile-zoom" width="22" height="22" viewBox="0 0 22 22"><circle cx="9" cy="9" r="8" fill="none" stroke="#999"/><path d="M9 5V13M5 9H13M15 15L21 21" stroke="#999"/></svg>
      <div class="tile-title">Products</div><div class="tile-label">Minimal price</div>
      <div class="tile-stats"><span class="likes">5 likes</span>&nbsp; 0 comments 0 pods</div>
      <div class="tile-price">$ 24</div><div class="tile-rule"></div>
    </article>
    <article class="tile" style="left:899px;top:55px">
      <div class="tile-photo" role="img" aria-label="Three bottles of red nail polish" style="background:linear-gradient(90deg,#fafafa,#b0153f 30%,#fafafa 50%,#b0153f 70%,#fafafa)"></div>
      <svg class="tile-zoom" width="22" height="22" viewBox="0 0 22 22"><circle cx="9" cy="9" r="8" fill="none" stroke="#999"/><path d="M9 5V13M5 9H13M15 15L21 21" stroke="#999"/></svg>
      <div class="tile-title">Products</div><div class="tile-label">Minimal price</div>
      <div class="tile-stats"><span class="likes">5 likes</span>&nbsp; 0 comments 0 pods</div>
      <div class="tile-price">$ 110</div><div class="tile-rule"></div>
    </article>

    <div class="row-rule"></div>

    <article class="tile" style="left:18px;top:342px">
      <div class="tile-photo" role="img" aria-label="Black and white toy box and printed bag" style="background:linear-gradient(135deg,#8a8a8a,#e8e8e8 50%,#7a7a7a)"></div>
      <svg class="tile-zoom" width="22" height="22" viewBox="0 0 22 22"><circle cx="9" cy="9" r="8" fill="none" stroke="#999"/><path d="M9 5V13M5 9H13M15 15L21 21" stroke="#999"/></svg>
      <div class="tile-title">Products</div><div class="tile-label">Minimal price</div>
      <div class="tile-stats"><span class="likes">5 likes</span>&nbsp; 0 comments 0 pods</div>
      <div class="tile-price">$ 60</div><div class="tile-rule"></div>
    </article>
    <article class="tile" style="left:238px;top:342px">
      <div class="tile-photo" role="img" aria-label="Gift box with tissue paper and shirt" style="background:linear-gradient(135deg,#a9a295,#ecebe4 55%,#b5a77a)"></div>
      <svg class="tile-zoom" width="22" height="22" viewBox="0 0 22 22"><circle cx="9" cy="9" r="8" fill="none" stroke="#999"/><path d="M9 5V13M5 9H13M15 15L21 21" stroke="#999"/></svg>
      <div class="tile-title">Products</div><div class="tile-label">Minimal price</div>
      <div class="tile-stats"><span class="likes">5 likes</span>&nbsp; 0 comments 0 pods</div>
      <div class="tile-price">$ 75</div><div class="tile-rule"></div>
    </article>
    <article class="tile" style="left:459px;top:342px">
      <div class="tile-photo" role="img" aria-label="Dark tablet case packaging boxes" style="background:linear-gradient(#f4f4f4,#4a4a4a 60%,#eaeaea)"></div>
      <svg class="tile-zoom" width="22" height="22" viewBox="0 0 22 22"><circle cx="9" cy="9" r="8" fill="none" stroke="#999"/><path d="M9 5V13M5 9H13M15 15L21 21" stroke="#999"/></svg>
      <div class="tile-title">Products</div><div class="tile-label">Minimal price</div>
      <div class="tile-stats"><span class="likes">5 likes</span>&nbsp; 0 comments 0 pods</div>
      <div class="tile-price">$ 60</div><div class="tile-rule"></div>
    </article>
    <article class="tile" style="left:678px;top:342px">
      <div class="tile-photo" role="img" aria-label="Baby bodysuit, gift bag and cards" style="background:linear-gradient(135deg,#f3efe8,#ffffff 55%,#e9eef4)"></div>
      <svg class="tile-zoom" width="22" height="22" viewBox="0 0 22 22"><circle cx="9" cy="9" r="8" fill="none" stroke="#999"/><path d="M9 5V13M5 9H13M15 15L21 21" stroke="#999"/></svg>
      <div class="tile-title">Products</div><div class="tile-label">Minimal price</div>
      <div class="tile-stats"><span class="likes">5 likes</span>&nbsp; 0 comments <span class="pods">2 pods</span></div>
      <div class="tile-price">$ 40</div><div class="tile-rule"></div>
    </article>
    <article class="tile" style="left:899px;top:342px">
      <div class="tile-photo" role="img" aria-label="Colourful packaged toys on cardboard" style="background:linear-gradient(90deg,#e86a2a,#b08a5a 35%,#3fb3e8 65%,#7fd83a)"></div>
      <svg class="tile-zoom" width="22" height="22" viewBox="0 0 22 22"><circle cx="9" cy="9" r="8" fill="none" stroke="#ddd"/><path d="M9 5V13M5 9H13M15 15L21 21" stroke="#ddd"/></svg>
      <div class="tile-title">Products</div><div class="tile-label">Minimal price</div>
      <div class="tile-stats"><span class="likes">5 likes</span>&nbsp; 0 comments 0 pods</div>
      <div class="tile-price">$ 30</div><div class="tile-rule"></div>
    </article>

    <div class="pager">
      <span class="count">123 products found</span>
      <span>view 10 per page</span>
      <span class="pages"><span class="current">1</span><span>2</span><span>3</span><span>4</span><span>...</span><span>22</span></span>
    </div>
    <div class="next">
      <svg width="6" height="10" viewBox="0 0 6 10"><path d="M6 0V10L0 5Z" fill="#6d8587"/></svg>
      <span>next</span>
      <svg width="6" height="10" viewBox="0 0 6 10"><path d="M0 0V10L6 5Z" fill="#6d8587"/></svg>
    </div>
  </main>

  <div class="payments">
    <span>Parcelpay</span><span>Ambrex</span><span>CoinPal</span><span>Mintcard</span><span>Vireo</span><span>Vireo Go</span><span>Vireo</span><span>Maxcard</span>
  </div>

  <footer>
    <nav class="footer-links"><a>Home</a><a>Site Map</a><a>About Us</a><a>Contacts</a></nav>
    <div class="footer-legal">2012 zantelope | All right reservet</div>
  </footer>
</div>
</body>
</html>
```